High-end construction company needs a business card design

We need a modern looking business card that draws people in, is memorable and looks so good people will want to sick it on their fridges.
On the first side what is needed are:
Logo
My name - Tomas Verbelk
Title - Managing Director
Website - www.kravel.co.uk
Email - tomas@kravel.co.uk
Telephone - 020 5194 6381
Mobile - 07845319027
On the back side was is needed is a list of all the services we provide:
-Kitchen Renovations
-Bathroom Renovations
-House Renovations
-Garage Conversions
-Extensions
-Loft Conversions
-Conservatories
-Carpentry
-Tiling
-Electrical
-Plumbing & Heating
-Bricklaying
-Landscaping
-Decorating
-Plastering
We would like the colours to be the same shades as on the logo with grey or black for the words.
Target Market(s)
Anyone who needs building work done
Contact Information for Business Card
This business card is for a construction company which strives to deliver excellent service and quality.
The look and feel of the card should represent this.
Requirements
Must have
- On the first side what is needed are:
Logo
My name - Tomas Verbelk
Title - Managing Director
Website - www.kravel.co.uk
Email - tomas@kravel.co.uk
Telephone - 020 5194 6381
Mobile - 07845319027
Nice to have
- Cool looking features

```html
<!DOCTYPE html>
<html lang="en">
<head>
<meta charset="utf-8">
<title>Kravel Construction Ltd – Business Card</title>
<link href="https://fonts.googleapis.com/css2?family=Open+Sans:wght@400;700&display=swap" rel="stylesheet">
<style>
  :root{
    --page:#e4e6e3;
    --green:#4a8f3f;
    --green-light:#7dc142;
    --green-pale:#a9d978;
    --white:#ffffff;
    --ink:#3d7a33;
  }
  *{box-sizing:border-box;margin:0;padding:0}
  html,body{width:1200px;height:1126px;overflow:hidden;background:var(--page);font-family:"Open Sans",Arial,sans-serif}
  .card{position:absolute;left:150px;width:900px;height:515px;overflow:hidden;box-shadow:0 6px 18px rgba(0,0,0,.18)}
  .card--back{top:30px;background:var(--green)}
  .card--front{top:581px;background:var(--white)}

  /* brand name in place of the mark */
  .brand{font-weight:700;line-height:1.1;text-transform:uppercase;letter-spacing:.04em;display:flex;align-items:center;gap:14px}
  .brand__dot{width:16px;height:16px;flex:none}
  .card--back .brand{position:absolute;left:0;right:0;top:70px;justify-content:center;color:var(--white);font-size:40px;text-align:center}
  .card--back .brand__dot{background:var(--white)}
  .card--front .brand{position:absolute;left:90px;top:95px;color:var(--green-light);font-size:30px}
  .card--front .brand__dot{background:var(--green-light)}

  /* services */
  .services{position:absolute;top:250px;left:70px;right:40px;display:flex;gap:50px}
  .services__col{list-style:none}
  .services__item{color:var(--white);font-size:22px;line-height:1.5;padding-left:28px;position:relative;white-space:nowrap}
  .services__item::before{content:"";position:absolute;left:0;top:12px;border-left:8px solid transparent;border-right:8px solid transparent;border-top:11px solid var(--green-light)}

  /* front */
  .band{position:absolute;left:0;right:0;top:250px;bottom:0;background:var(--green)}
  .band__notch{position:absolute;left:220px;top:0;border-left:22px solid transparent;border-right:22px solid transparent;border-top:22px solid var(--white)}
  .person{position:absolute;right:110px;top:110px;text-align:left}
  .person__bar{width:62px;height:8px;background:var(--green-light);margin:0 0 18px 95px}
  .person__name{font-size:30px;font-weight:700;color:var(--ink);white-space:nowrap}
  .person__title{font-size:22px;color:var(--green-light);white-space:nowrap}
  .contacts{position:absolute;left:90px;top:55px;list-style:none;z-index:1}
  .contacts__item{display:flex;align-items:center;gap:14px;color:var(--white);font-size:23px;line-height:1.4;white-space:nowrap}
  .contacts__icon{width:18px;height:18px;flex:none}
  .artwork{position:absolute;left:0;top:0}
</style>
</head>
<body>

<section class="card card--back">
  <div class="brand"><span class="brand__dot"></span><span>Kravel<br>Construction Ltd</span></div>
  <div class="services">
    <ul class="services__col">
      <li class="services__item">Kitchen Renovations</li>
      <li class="services__item">Bathroom Renovations</li>
      <li class="services__item">House Renovations</li>
      <li class="services__item">Garage Conversions</li>
      <li class="services__item">Extensions</li>
    </ul>
    <ul class="services__col">
      <li class="services__item">Plumbing &amp; Heating</li>
      <li class="services__item">Bricklaying</li>
      <li class="services__item">Landscaping</li>
      <li class="services__item">Decorating</li>
      <li class="services__item">Plastering</li>
    </ul>
    <ul class="services__col">
      <li class="services__item">Loft Conversions</li>
      <li class="services__item">Conservatories</li>
      <li class="services__item">Carpentry</li>
      <li class="services__item">Tiling</li>
      <li class="services__item">Electrical</li>
    </ul>
  </div>
</section>

<section class="card card--front">
  <div class="brand"><span class="brand__dot"></span><span>Kravel<br>Construction Ltd</span></div>
  <div class="person">
    <div class="person__bar"></div>
    <div class="person__name">Tomas Verbelk</div>
    <div class="person__title">Managing Director</div>
  </div>
  <div class="band">
    <span class="band__notch"></span>
    <svg class="artwork" width="900" height="265" viewBox="0 0 900 265" role="img" aria-label="Illustration of an excavator arm over a house and city buildings">
      <defs>
        <linearGradient id="artFill" x1="0" y1="1" x2="1" y2="0">
          <stop offset="0" stop-color="#5fa84a"/>
          <stop offset="1" stop-color="#8fcf5a"/>
        </linearGradient>
      </defs>
      <polygon points="400,265 650,110 790,50 900,120 900,265" fill="url(#artFill)"/>
    </svg>
    <ul class="contacts">
      <li class="contacts__item">
        <svg class="contacts__icon" viewBox="0 0 24 24"><path fill="#a9d978" d="M6.6 10.8a15 15 0 0 0 6.6 6.6l2.2-2.2c.3-.3.7-.4 1-.2 1.1.4 2.3.6 3.6.6.6 0 1 .4 1 1V20c0 .6-.4 1-1 1A17 17 0 0 1 3 4c0-.6.4-1 1-1h3.5c.6 0 1 .4 1 1 0 1.3.2 2.5.6 3.6.1.3 0 .7-.2 1z"/></svg>
        020 5194 6381</li>
      <li class="contacts__item">
        <svg class="contacts__icon" viewBox="0 0 24 24"><rect x="6" y="2" width="12" height="20" rx="2" fill="none" stroke="#a9d978" stroke-width="2"/><circle cx="12" cy="18" r="1.2" fill="#a9d978"/></svg>
        07845319027</li>
      <li class="contacts__item">
        <svg class="contacts__icon" viewBox="0 0 24 24"><rect x="2" y="5" width="20" height="14" fill="none" stroke="#a9d978" stroke-width="2"/><path d="M2 5l10 8 10-8" fill="none" stroke="#a9d978" stroke-width="2"/></svg>
        tomas@kravel.co.uk</li>
      <li class="contacts__item">
        <svg class="contacts__icon" viewBox="0 0 24 24"><circle cx="12" cy="12" r="10" fill="none" stroke="#a9d978" stroke-width="2"/><path d="M2 12h20M12 2c3 3 3 17 0 20M12 2c-3 3-3 17 0 20" fill="none" stroke="#a9d978" stroke-width="1.6"/></svg>
        www.kravel.co.uk</li>
    </ul>
  </div>
</section>

</body>
</html>
```